fresh noodle packaging

we need to rebrand our existing brand which base for asia market in australia, we need a fresher look which market for more western style.

i attached our existing product, involved two logo, we want to make all design into one brand only, ( Lin Bo instead of noodle harwick)

requirement:
trendy
fresh
economical
" looks" enviromental friendly
cost effective

one design as a signature and represent the company, expect to fit all type of noodle except text and color

Target Market(s)

supermarket e.g valmarto

Requirements
Must have
• remain color from our old packaging

```html
<!DOCTYPE html>
<html lang="en">
<head>
<meta charset="utf-8">
<title>Hokkien Noodle Packaging – Label Options</title>
<link href="https://fonts.googleapis.com/css2?family=Bungee&family=Permanent+Marker&family=Roboto+Slab:wght@500;700&family=Open+Sans:wght@600&display=swap" rel="stylesheet">
<style>
  :root {
    --navy: #15175f;
    --red: #cc0000;
    --art-light: #f6d3d3;
    --art-deep: #e59a9a;
    --white: #ffffff;
    --paper: #f2f2f2;
    --stage: #e4e4e4;
    --ink: #111111;
    --caption: #555555;
  }
  * { margin: 0; padding: 0; box-sizing: border-box; }
  html, body { width: 1200px; height: 848px; overflow: hidden; }
  body {
    background: radial-gradient(ellipse at center, #f4f4f4 0%, var(--stage) 100%);
    position: relative;
    font-family: "Roboto Slab", serif;
  }
  .label {
    position: absolute; top: 96px; width: 488px; height: 648px;
    border: 4px solid var(--navy); border-radius: 36px;
    background: linear-gradient(180deg, #fafafa, var(--paper));
    overflow: hidden;
  }
  .label--wave { left: 84px; }
  .label--clean { left: 630px; }
  .label > * { position: absolute; white-space: nowrap; }
  .logo-mark {
    left: 44px; top: 47px; width: 80px; height: 80px; border-radius: 50%;
    background: var(--red); color: var(--white);
    display: flex; flex-direction: column; align-items: center; justify-content: center;
    font-family: "Bungee", sans-serif; font-size: 15px; line-height: 1.1;
  }
  .brand-word {
    left: 166px; top: 30px; font-family: "Bungee", sans-serif;
    font-size: 74px; line-height: 1; color: var(--red); letter-spacing: 1px;
  }
  .brand-sub {
    left: 254px; top: 104px; font-family: "Permanent Marker", cursive;
    font-size: 30px; line-height: 1; color: var(--navy); letter-spacing: 2px;
  }
  .product-line1, .product-line2 { font-family: "Bungee", sans-serif; line-height: 1; }
  .product-line1 { color: var(--navy); }
  .product-line2 { color: var(--red); }
  .chef-art {
    background: linear-gradient(160deg, var(--art-light) 0%, var(--art-deep) 100%);
  }
  .chef-art--large {
    left: 175px; top: 214px; width: 305px; height: 312px;
    clip-path: polygon(38% 0, 100% 0, 100% 100%, 20% 100%, 0 55%, 12% 48%, 38% 48%);
  }
  .chef-art--small {
    left: 146px; top: 166px; width: 178px; height: 168px;
    clip-path: polygon(40% 0, 100% 5%, 100% 80%, 75% 88%, 10% 100%, 0 45%, 30% 45%);
  }
  .wave { left: 0; top: 0; width: 480px; height: 640px; }
  .cert-seal { border-radius: 50%; }
  .info-left { font-weight: 500; font-size: 10.5px; line-height: 1.2; text-transform: uppercase; }
  .codes { font-weight: 500; font-size: 9px; line-height: 1.25; color: var(--red); }
  .net { font-weight: 700; font-size: 18px; line-height: 1; }
  .tagline { font-weight: 500; font-size: 18.5px; line-height: 1.05; color: var(--red); text-align: right; text-transform: uppercase; }
  .maker { font-family: "Permanent Marker", cursive; font-size: 16px; line-height: 1; letter-spacing: 1.5px; }
  .address { font-weight: 500; font-size: 9px; line-height: 1; }
  .no-pres { font-weight: 500; font-size: 11px; color: var(--white); }
  .no-pres-vertical {
    font-family: "Permanent Marker", cursive; font-size: 14px; line-height: 1; color: var(--navy);
    writing-mode: vertical-rl; transform: rotate(180deg); letter-spacing: 1.5px;
  }
  .caption {
    position: absolute; top: 788px; width: 300px; text-align: center;
    font-family: "Open Sans", sans-serif; font-weight: 600; font-size: 21px; color: var(--caption);
  }
</style>
</head>
<body>

<!-- Option 1: navy wave base -->
<section class="label label--wave">
  <div class="chef-art chef-art--large" role="img" aria-label="Red line illustration of a smiling chef making an OK hand sign"></div>
  <svg class="wave" viewBox="0 0 480 640" aria-hidden="true">
    <path d="M0,372 C60,470 180,528 300,526 C380,524 440,508 480,498 L480,640 L0,640 Z" fill="var(--navy)"/>
    <path d="M0,356 C60,462 180,520 300,518 C380,516 440,500 480,490" fill="none" stroke="var(--red)" stroke-width="5"/>
  </svg>
  <div class="logo-mark"><span>LOGO</span><span>HERE</span></div>
  <div class="brand-word">BRAND</div>
  <div class="brand-sub">NAME HERE</div>
  <div class="product-line1" style="left:17px;top:222px;font-size:52px;">HOKKIEN</div>
  <div class="product-line2" style="left:51px;top:274px;font-size:52px;">NOODLE</div>
  <svg style="left:109px;top:329px;" width="175" height="26" viewBox="0 0 175 26" aria-hidden="true">
    <path d="M0,24 C50,4 130,0 175,16 C130,8 60,10 0,24 Z" fill="var(--red)"/>
  </svg>
  <div class="cert-seal" style="left:20px;top:494px;width:62px;height:62px;border:2px solid var(--white);"></div>
  <div class="info-left" style="left:17px;top:574px;color:var(--white);">Lorem ipsum simply<br>dummy text</div>
  <div class="codes" style="left:17px;top:604px;">ABC-XXX-XXX-XX<br>EFG-XXX-XXX-XX</div>
  <div class="no-pres" style="left:182px;top:581px;">No Preservatives</div>
  <div style="left:176px;top:595px;width:104px;height:32px;border:2px solid var(--white);border-radius:3px;"></div>
  <div class="net" style="right:10px;top:536px;color:var(--white);">Net : 2 kg</div>
  <div class="tagline" style="right:6px;top:560px;">Lorem ipsum<br>dummy text</div>
  <div class="maker" style="right:8px;top:604px;color:var(--white);">LIN BO FOOD MFR</div>
  <div class="address" style="right:18px;top:626px;color:var(--white);">Your Company Address Goes Here</div>
</section>

<!-- Option 2: clean white -->
<section class="label label--clean">
  <div class="logo-mark"><span>LOGO</span><span>HERE</span></div>
  <div class="brand-word">BRAND</div>
  <div class="brand-sub">NAME HERE</div>
  <div class="chef-art chef-art--small" role="img" aria-label="Red line illustration of a smiling chef making an OK hand sign"></div>
  <div class="no-pres-vertical" style="left:449px;top:170px;">NO PRESERVATIVES</div>
  <div style="left:431px;top:360px;width:42px;height:136px;border:2px solid var(--navy);border-radius:3px;"></div>
  <div class="product-line1" style="left:66px;top:343px;font-size:64px;">HOKKIEN</div>
  <div class="product-line2" style="left:106px;top:401px;font-size:64px;">NOODLE</div>
  <svg style="left:176px;top:470px;" width="212" height="26" viewBox="0 0 212 26" aria-hidden="true">
    <path d="M0,24 C60,4 150,0 212,16 C160,8 70,10 0,24 Z" fill="var(--red)"/>
  </svg>
  <div class="cert-seal" style="left:19px;top:493px;width:58px;height:58px;border:2px solid var(--red);"></div>
  <div class="info-left" style="left:19px;top:576px;color:var(--navy);font-size:12px;">Lorem ipsum simply<br>dummy text</div>
  <div class="codes" style="left:19px;top:610px;">ABC-XXX-XXX-XX<br>EFG-XXX-XXX-XX</div>
  <div class="net" style="right:16px;top:526px;color:var(--ink);font-size:20px;">Net : 2 kg</div>
  <div class="tagline" style="right:14px;top:550px;">Lorem ipsum<br>dummy text</div>
  <div class="maker" style="right:18px;top:602px;color:var(--navy);">LIN BO FOOD MFR</div>
  <div class="address" style="right:38px;top:625px;color:var(--ink);">Your Company Address Goes Here</div>
</section>

<div class="caption" style="left:178px;">SAMPLE 1</div>
<div class="caption" style="left:724px;">SAMPLE 2</div>

</body>
</html>
```